Harborline 52 Sailing Magazine

I need a magazine layout for a new sailing magazine (called 'Harborline 52'). I would like to see designs for both the cover as well as the inside spread and the template should allow for content to be dropped into it. Please note that on an ongoing basis, I would prefer to provide the content to the designer, who then adds it to the template, making the necessary edits).

Colors

Designer to choose colors to be used in the design.

Requirements
Must have
• Classy modern design, nautical colors and theme (but clean and modern)
Should not have
• Tacky, old school sailing stuff. Also, here is a great example of how I don't want it to look! Like so many other magazines, the ads take over and give the magazine a very unsophisticated feel. Click on the magazine at this website to see it's inside pages:
• https://www.windquaymag.example/

```html
<!DOCTYPE html>
<html lang="en">
<head>
<meta charset="utf-8">
<title>Harborline 52 — Cover and Inside Spread</title>
<link rel="stylesheet" href="https://fonts.googleapis.com/css2?family=Roboto+Slab:wght@300;800&family=Montserrat:wght@800&family=Open+Sans:ital,wght@0,400;0,700;1,800&display=swap">
<style>
  :root {
    --backdrop: #8c8c8c;
    --paper: #ffffff;
    --navy: #0d4f8b;
    --band: rgba(120, 160, 200, 0.72);
    --ink: #111111;
    --body-ink: #222222;
    --caption-ink: #555555;
    --sky-top: #c9d3dc;
    --sky-mid: #e8ecef;
    --sea-top: #5a8ea6;
    --sea-deep: #1f4f66;
  }
  * { box-sizing: border-box; margin: 0; padding: 0; }
  html, body { width: 955px; height: 1200px; overflow: hidden; }
  body { background: var(--backdrop); position: relative; font-family: "Open Sans", Arial, sans-serif; }

  /* ---------- Cover ---------- */
  .cover {
    position: absolute; left: 257px; top: 28px; width: 440px; height: 562px;
    overflow: hidden; background: var(--paper); box-shadow: 0 6px 18px rgba(0,0,0,0.35);
  }
  .cover-photo {
    position: absolute; inset: 0;
    background: linear-gradient(180deg, var(--sky-top) 0%, var(--sky-mid) 30%, #d7dfe5 52%, var(--sea-top) 56%, var(--sea-deep) 100%);
  }
  .cover-band {
    position: absolute; left: 0; top: 0; width: 100px; height: 100%;
    background: var(--band);
  }
  .cover-title {
    position: absolute; left: 50px; bottom: 24px;
    transform-origin: left bottom; transform: rotate(-90deg) translateY(50%);
    font-family: "Roboto Slab", Georgia, serif; font-weight: 300;
    font-size: 56px; letter-spacing: 4px; color: var(--paper); white-space: nowrap; line-height: 1;
  }
  .cover-issue {
    position: absolute; left: 112px; top: 20px;
    font-family: "Roboto Slab", Georgia, serif; font-weight: 300; font-size: 84px; line-height: 1;
    color: rgba(255,255,255,0.35); -webkit-text-stroke: 1.5px #f2f4f6;
  }
  .cover-year {
    position: absolute; right: 22px; bottom: 22px;
    font-family: "Roboto Slab", Georgia, serif; font-weight: 800; font-size: 60px;
    letter-spacing: 10px; color: var(--paper); line-height: 1;
  }

  /* ---------- Spread ---------- */
  .spread {
    position: absolute; left: 37px; top: 620px; width: 880px; height: 552px;
    box-shadow: 0 6px 18px rgba(0,0,0,0.35);
  }
  .page { position: absolute; top: 0; width: 440px; height: 552px; background: var(--paper); }
  .page-left { left: 0; }
  .page-right { left: 440px; background: linear-gradient(90deg, #e9e9e9 0, var(--paper) 14px); }
  .page-left::after {
    content: ""; position: absolute; right: 0; top: 0; width: 14px; height: 100%;
    background: linear-gradient(90deg, transparent, #e6e6e6);
  }

  .masthead-tab {
    position: absolute; left: 30px; top: 0; height: 24px; padding: 0 14px 0 12px;
    background: var(--navy); color: var(--paper);
    font-weight: 700; font-size: 15px; line-height: 24px; letter-spacing: 0.5px;
  }
  .article-title {
    position: absolute; left: 100px; top: 100px;
    font-family: "Montserrat", Arial, sans-serif; font-weight: 800;
    font-size: 40px; line-height: 0.98; color: var(--navy);
  }
  .pull-quote {
    position: absolute; left: 48px; top: 262px; width: 100px;
    font-style: italic; font-weight: 800; font-size: 13.5px; line-height: 1.2;
    color: var(--ink); text-align: right;
  }
  .pull-quote .quote-mark {
    float: left; font-family: Georgia, serif; font-style: normal; font-weight: 700;
    font-size: 54px; line-height: 0.75; margin-top: 2px; margin-right: 2px;
  }
  .body-column {
    position: absolute; font-size: 6.8px; line-height: 1.16; color: var(--body-ink); text-align: justify;
  }
  .body-column p + p { margin-top: 8px; }
  .drop-cap { float: left; font-weight: 700; font-size: 22px; line-height: 0.85; margin-right: 2px; color: var(--ink); }
  .lead-in { font-weight: 700; }
  .col-left { left: 165px; top: 226px; width: 108px; }
  .col-right { left: 278px; top: 258px; width: 122px; }

  .feature-photo {
    position: absolute; left: 285px; top: 208px; width: 420px; height: 300px;
    background: linear-gradient(180deg, #3f7fc4 0%, #6fa3d8 30%, #cfe0ef 50%, #7c9bb5 62%, #1d4f86 70%, #143d6c 100%);
  }
  .detail-photo {
    position: absolute; left: 115px; top: 62px; width: 280px; height: 138px;
    background: linear-gradient(180deg, #9aaebf 0%, #d5dde4 40%, #b3c1cc 60%, #4e6f84 68%, #2c4d62 100%);
  }
  .photo-caption {
    position: absolute; left: 6px; top: 158px; width: 104px;
    font-size: 5.2px; line-height: 1.2; color: var(--caption-ink); text-align: right; font-weight: 700;
  }

  .page-footer {
    position: absolute; left: 0; right: 0; bottom: 14px; height: 8px; background: var(--navy);
  }
  .page-number {
    position: absolute; left: 30px; bottom: 14px; height: 8px; line-height: 8px;
    font-size: 5.5px; font-weight: 700; color: var(--paper); letter-spacing: 0.3px;
  }
</style>
</head>
<body>

  <section class="cover">
    <div class="cover-photo" role="img" aria-label="Photograph of a white catamaran under full sail on a blue sea beneath a cloudy sky"></div>
    <div class="cover-band"></div>
    <div class="cover-title">HARBORLINE</div>
    <div class="cover-issue">52</div>
    <div class="cover-year">2020</div>
  </section>

  <section class="spread">
    <article class="page page-left">
      <div class="masthead-tab">HARBORLINE 52</div>
      <h1 class="article-title">YOUR<br>TILTLE HERE</h1>

      <blockquote class="pull-quote">
        <span class="quote-mark">&ldquo;</span>Lorem Ipsum is simply dummy text of the printing and typesetting industry Lorem Ipsum is simply dummy
      </blockquote>

      <div class="body-column col-left">
        <p><span class="drop-cap">L</span>orem Ipsum is simply dummy text of the printing and typesetting industry. Lorem Ipsum has been the industry's standard dummy text ever since the 1500s, when an unknown printer took a galley of type and scrambled it to make a type specimen book. It has survived not only five centuries, but also the leap into electronic typesetting, remaining essentially unchanged.</p>
        <p>It was popularised in the 1960s with the release of Typeframe sheets containing Lorem Ipsum passages, and more recently with desktop publishing software like Quillset Layout including versions of Lorem Ipsum.</p>
        <p>Lorem Ipsum is simply dummy text of the printing and typesetting industry. Lorem Ipsum has been the industry's standard dummy text ever since the 1500 versions of Lorem Ipsum.</p>
      </div>

      <div class="page-footer"></div>
      <div class="page-number">PAGE 1</div>
    </article>

    <article class="page page-right">
      <div class="detail-photo" role="img" aria-label="Photograph of a catamaran sailing on open water under a grey cloudy sky"></div>
      <p class="photo-caption">Lorem Ipsum is simply dummy text of the printing and typesetting industry. Lorem Ipsum has been the industry's standard dummy text ever since the 1500 versions of Lorem Ipsum.</p>

      <div class="body-column col-right">
        <p><span class="lead-in">L</span>orem Ipsum is simply dummy text of the printing and typesetting industry. Lorem Ipsum has been the industry's standard dummy text ever since the 1500s, when an unknown printer took a galley of type and scrambled it to make a type specimen book. It has survived not only five centuries, but also the leap into electronic typesetting, remaining essentially unchanged.</p>
        <p>It was popularised in the 1960s with the release of Typeframe sheets containing Lorem Ipsum passages, and more recently with desktop publishing software like Quillset Layout including versions of Lorem Ipsum.</p>
        <p>Lorem Ipsum is simply dummy text of the printing and typesetting industry. Lorem Ipsum has been the industry's standard dummy text ever since the 1500 versions of Lorem Ipsum.</p>
      </div>

      <div class="page-footer"></div>
      <div class="page-number">PAGE 1</div>
    </article>

    <div class="feature-photo" role="img" aria-label="Photograph of a sailing yacht with white sails on a deep blue sea under a bright sky with white clouds and distant hills"></div>
  </section>

</body>
</html>
```